Cobalt Field Services website design

We want to create a Sports turf website for our business Cobalt Field Services - we do sports turf management on sports fields around the Mackay region soccer rugby league softball fields etc from full turf management plans and maintenance to just supply and apply of turf management products and just supply of products with program we also do grounds facility maintenance at council facility's and grounds that require a higher level of care - we will up load our logos and fonts etc to assist with the colour pallet for the website - we will have to have a landing page a shop page with tabs a gallery tab along with a grants initiative and our northreach finest green tab also - our font for the txt is called ethnocentric
Updates

how do we open time for people to submit we have no one submitted

Industry/Entity Type

Turf

Coding

Coded - Design and coding required

Number of Pages Required

5+ page

Font styles to use
Other font styles liked:
• ethnocentric

Requirements
Must have
• I have mentioned some waffle in the description that should assist
Should not have
• anything not related

```html
<!DOCTYPE html>
<html lang="en">
<head>
<meta charset="utf-8">
<title>Cobalt Field Services – Website Pages</title>
<link href="https://fonts.googleapis.com/css2?family=Orbitron:wght@500;600;700&family=Inter:ital,wght@0,400;0,500;0,600;0,700;1,700&display=swap" rel="stylesheet">
<style>
:root{
  --green:#1a9a48;
  --green-dark:#137a3a;
  --green-light:#22b455;
  --ink:#1f1f1f;
  --muted:#777;
  --line:#e6e6e6;
  --soft:#f4f4f4;
  --white:#fff;
  --btn-grey:#8a8a8a;
}
*{box-sizing:border-box;margin:0;padding:0}
html,body{width:1200px;height:1200px;overflow:hidden;background:var(--white)}
body{font-family:"Inter",Arial,sans-serif;color:var(--ink)}
.stage{position:absolute;left:0;top:0;width:1932px;height:1932px;transform:scale(.6211);transform-origin:0 0}
.page{position:absolute;overflow:hidden;background:var(--white)}
.page *{position:absolute}
.c{text-align:center}
.display{font-family:"Orbitron",sans-serif;font-weight:600;letter-spacing:1.5px;line-height:1.1;white-space:nowrap}
.nav{left:0;right:0;height:38px;background:var(--white);border-bottom:1px solid var(--line)}
.nav .brand{font-size:9px;font-weight:600;color:#9ccfa9;line-height:1}
.nav .link{font-size:8px;color:#333;white-space:nowrap;line-height:1}
.nav .link.on{color:var(--green)}
.nav .quote{background:var(--green);color:var(--white);font-size:7.5px;font-weight:600;border-radius:3px;line-height:19px;text-align:center}
.sub{font-size:10px;color:var(--muted);line-height:1.45}
.small{font-size:7.5px;color:var(--muted);line-height:1.55}
.card{background:var(--white);border:1px solid var(--line);border-radius:4px}
.card-title{font-size:10px;font-weight:700;color:var(--ink);white-space:nowrap}
.icon{color:var(--green);fill:none;stroke:currentColor;stroke-width:1.8;stroke-linecap:round;stroke-linejoin:round}
.cta{background:linear-gradient(135deg,var(--green-light),var(--green-dark))}
.on-green{color:var(--white)}
.lead{font-size:9px;color:var(--white);line-height:1.55}
.btn-grey{background:var(--btn-grey);color:var(--white);font-size:7.5px;font-weight:600;border-radius:3px;text-align:center}
.btn-green{background:var(--green);color:var(--white);font-size:7.5px;font-weight:600;border-radius:3px;text-align:center}
.btn-line{border:1px solid var(--white);color:var(--white);font-size:7.5px;font-weight:600;border-radius:3px;text-align:center}
.photo{border-radius:2px;background:linear-gradient(135deg,#6aa84a 0%,#3f8a2e 100%)}
.grass{background:linear-gradient(160deg,#b8d9a6 0%,#6fb24c 35%,#3f8f2c 70%,#2e7a22 100%)}
.grass-soft{background:linear-gradient(120deg,#e6f1e1 0%,#c9e3bd 45%,#9fcf88 100%)}
.price{font-size:13px;font-weight:700;color:var(--green)}
.cart-ico{position:relative !important;top:2px;width:8px;height:8px;fill:none;stroke:#fff;stroke-width:2.4}
</style>
</head>
<body>
<svg width="0" height="0" style="position:absolute">
  <defs>
    <symbol id="i-trophy" viewBox="0 0 24 24"><path d="M8 21h8M12 17v4M7 4h10v5a5 5 0 0 1-10 0zM7 6H4a3 3 0 0 0 3 4M17 6h3a3 3 0 0 1-3 4"/></symbol>
    <symbol id="i-clip" viewBox="0 0 24 24"><rect x="5" y="4" width="14" height="17" rx="2"/><rect x="9" y="2" width="6" height="4" rx="1"/><path d="M9 13l2 2 4-4"/></symbol>
    <symbol id="i-file" viewBox="0 0 24 24"><path d="M14 2H6a2 2 0 0 0-2 2v16a2 2 0 0 0 2 2h12a2 2 0 0 0 2-2V8z"/><path d="M14 2v6h6M8 13h8M8 17h8M8 9h2"/></symbol>
    <symbol id="i-box" viewBox="0 0 24 24"><path d="M21 8l-9-5-9 5v8l9 5 9-5z"/><path d="M3 8l9 5 9-5M12 13v8M7.5 5.5l9 5"/></symbol>
    <symbol id="i-bag" viewBox="0 0 24 24"><rect x="4" y="4" width="16" height="17" rx="2"/><path d="M4 8h16M9 11a3 3 0 0 0 6 0"/></symbol>
    <symbol id="i-hand" viewBox="0 0 24 24"><path d="M3 14l4-4 4 1 4-4 4 4-6 6H9l-3 3"/><path d="M11 11l3 3"/><circle cx="17" cy="5" r="2"/></symbol>
    <symbol id="i-trend" viewBox="0 0 24 24"><path d="M3 17l6-6 4 4 8-8M15 7h6v6"/></symbol>
    <symbol id="i-checkc" viewBox="0 0 24 24"><path d="M21 11.1V12a9 9 0 1 1-5.3-8.2"/><path d="M21 4L12 13l-3-3"/></symbol>
    <symbol id="i-star" viewBox="0 0 24 24"><path d="M12 2l3 6.5 7 .8-5.2 4.8 1.5 7-6.3-3.6-6.3 3.6 1.5-7L2 9.3l7-.8z"/></symbol>
    <symbol id="i-award" viewBox="0 0 24 24"><circle cx="12" cy="8" r="6"/><path d="M8.5 13L7 22l5-3 5 3-1.5-9"/></symbol>
    <symbol id="i-users" viewBox="0 0 24 24"><circle cx="9" cy="7" r="4"/><path d="M2 21v-2a4 4 0 0 1 4-4h6a4 4 0 0 1 4 4v2M16 3.1a4 4 0 0 1 0 7.8M22 21v-2a4 4 0 0 0-3-3.9"/></symbol>
    <symbol id="i-cart" viewBox="0 0 24 24"><circle cx="9" cy="20" r="1.5"/><circle cx="18" cy="20" r="1.5"/><path d="M2 3h3l2.7 12.4a2 2 0 0 0 2 1.6h7.8a2 2 0 0 0 2-1.6L21 7H6"/></symbol>
  </defs>
</svg>

<div class="stage">

<!-- HOME PAGE -->
<section class="page page-home" style="left:0;top:193px;width:643px;height:1072px">
  <div class="nav" style="top:4px">
    <div class="brand" style="left:14px;top:15px">CFS</div>
    <div class="link on" style="left:342px;top:15px">Home</div>
    <div class="link" style="left:377px;top:15px">Shop</div>
    <div class="link" style="left:409px;top:15px">Gallery</div>
    <div class="link" style="left:447px;top:15px">Grants Initiative</div>
    <div class="link" style="left:512px;top:15px">Northreach Green</div>
    <div class="quote" style="left:594px;top:9px;width:52px;height:19px">Get a Quote</div>
  </div>
  <div class="hero grass" role="img" aria-label="Sunlit sports field grass with goal posts" style="left:0;top:43px;width:643px;height:410px"></div>
  <div style="left:0;top:43px;width:643px;height:410px;background:linear-gradient(90deg,rgba(255,255,255,.82) 0%,rgba(255,255,255,.55) 45%,rgba(255,255,255,0) 85%)"></div>
  <h1 class="display" style="left:8px;top:137px;font-size:36px;color:var(--ink);letter-spacing:2px">COBALT FIELD<br>SERVICES</h1>
  <p style="left:9px;top:217px;font-size:15px;font-weight:700;font-style:italic;color:var(--green)">"Performance starts from the ground up."</p>
  <p style="left:8px;top:250px;width:340px;font-size:10px;color:#555;line-height:1.4">Leading sports turf management and maintenance for soccer, rugby league, softball fields, and sporting facilities across the Mackay region.</p>
  <div class="btn-green" style="left:8px;top:296px;width:72px;height:21px;line-height:21px;font-size:8.5px">Shop Now</div>
  <div style="left:89px;top:296px;width:79px;height:21px;line-height:21px;font-size:8.5px;background:var(--white);border-radius:3px;text-align:center;color:var(--ink)">Get a Quote</div>

  <div style="left:0;top:453px;width:643px;height:260px;background:var(--soft)"></div>
  <h2 class="display c" style="left:0;top:490px;width:655px;font-size:23px">OUR SERVICES</h2>
  <p class="sub c" style="left:0;top:522px;width:655px;font-size:8.5px">Professional turf management solutions for sports facilities across Mackay</p>
  <div class="card" style="left:8px;top:567px;width:150px;height:107px"></div>
  <div class="card" style="left:171px;top:567px;width:150px;height:107px"></div>
  <div class="card" style="left:333px;top:567px;width:150px;height:107px"></div>
  <div class="card" style="left:496px;top:567px;width:150px;height:107px"></div>
  <svg class="icon" style="left:21px;top:579px;width:20px;height:20px"><use href="#i-clip"/></svg>
  <svg class="icon" style="left:184px;top:579px;width:20px;height:20px"><use href="#i-file"/></svg>
  <svg class="icon" style="left:346px;top:579px;width:20px;height:20px"><use href="#i-box"/></svg>
  <svg class="icon" style="left:509px;top:579px;width:20px;height:20px"><use href="#i-bag"/></svg>
  <div class="card-title" style="left:20px;top:610px">Full Turf Management</div>
  <div class="card-title" style="left:182px;top:610px">Ongoing Maintenance</div>
  <div class="card-title" style="left:345px;top:610px">Supply &amp; Apply</div>
  <div class="card-title" style="left:508px;top:610px">Product Supply</div>
  <p class="small" style="left:20px;top:628px;width:130px">Comprehensive sports turf management plans tailored to your facility's needs</p>
  <p class="small" style="left:182px;top:628px;width:130px">Regular maintenance services to keep your fields in peak condition year-round</p>
  <p class="small" style="left:345px;top:628px;width:130px">Professional application of turf management products with expert precision</p>
  <p class="small" style="left:508px;top:628px;width:130px">Quality turf management products with complete maintenance programs</p>

  <div class="grass-soft" role="img" aria-label="Close-up of green grass blades" style="left:0;top:714px;width:643px;height:184px"></div>
  <h2 class="display c" style="left:0;top:750px;width:655px;font-size:23px">MACKAY'S TURF SPECIALISTS</h2>
  <div style="left:112px;top:790px;font-size:12px;font-weight:700;color:var(--green)">Expert Care</div>
  <div style="left:335px;top:790px;font-size:12px;font-weight:700;color:var(--green)">Council Facilities</div>
  <p class="small" style="left:112px;top:813px;width:200px;color:#666">We specialize in maintaining sports fields for soccer, rugby league, softball, and other sporting facilities, ensuring optimal playing conditions year-round.</p>
  <p class="small" style="left:335px;top:813px;width:210px;color:#666">Trusted by council facilities and high-care venues across the Mackay region for comprehensive grounds and facility maintenance services.</p>

  <div class="cta" style="left:0;top:897px;width:643px;height:175px"></div>
  <h2 class="display c on-green" style="left:0;top:934px;width:655px;font-size:21px">READY TO ELEVATE YOUR FIELD?</h2>
  <p class="lead c" style="left:160px;top:969px;width:335px;font-size:10px;line-height:1.4">Contact us today for a custom turf management plan tailored to your facility</p>
  <div class="btn-grey" style="left:289px;top:1013px;width:76px;height:20px;line-height:20px;font-size:8.5px">Get Started</div>
</section>

<!-- GRANTS PAGE -->
<section class="page page-grants" style="left:650px;top:183px;width:638px;height:1075px">
  <div class="nav" style="top:0;height:28px">
    <div class="brand" style="left:6px;top:6px">CFS</div>
    <div class="link" style="left:335px;top:6px">Home</div>
    <div class="link" style="left:369px;top:6px">Shop</div>
    <div class="link" style="left:401px;top:6px">Gallery</div>
    <div class="link on" style="left:439px;top:6px">Grants Initiative</div>
    <div class="link" style="left:505px;top:6px">Northreach Green</div>
    <div class="quote" style="left:586px;top:0;width:52px;height:19px">Get a Quote</div>
  </div>
  <h1 class="display c" style="left:0;top:38px;width:638px;font-size:29px;letter-spacing:2.5px">GRANTS INITIATIVE</h1>
  <p class="sub c" style="left:150px;top:79px;width:338px">Helping Mackay sports facilities access funding opportunities for turf improvement and maintenance projects</p>
  <div class="card" style="left:105px;top:138px;width:430px;height:147px"></div>
  <div style="left:117px;top:149px;font-size:14px;font-weight:500">Funding Your Turf Projects</div>
  <p class="small" style="left:117px;top:178px;width:405px">Cobalt Field Services partners with sports facilities across the Mackay region to help secure grant funding for turf improvement and maintenance projects.</p>
  <p class="small" style="left:117px;top:209px;width:405px">Whether you're looking to upgrade your existing fields, implement a comprehensive maintenance program, or completely renovate your sports facility, various grant opportunities are available to help make your project possible.</p>
  <p class="small" style="left:117px;top:251px;width:405px">Our team has extensive experience in grant applications and can guide you through the entire process, from identifying suitable funding sources to implementing approved projects.</p>

  <h2 class="display c" style="left:0;top:317px;width:638px;font-size:17px">HOW WE HELP</h2>
  <div class="card" style="left:0;top:359px;width:313px;height:104px"></div>
  <div class="card" style="left:325px;top:359px;width:313px;height:104px"></div>
  <div class="card" style="left:0;top:475px;width:313px;height:92px"></div>
  <div class="card" style="left:325px;top:475px;width:313px;height:92px"></div>
  <svg class="icon" style="left:16px;top:374px;width:22px;height:22px"><use href="#i-hand"/></svg>
  <svg class="icon" style="left:342px;top:374px;width:22px;height:22px"><use href="#i-file"/></svg>
  <svg class="icon" style="left:16px;top:491px;width:22px;height:22px"><use href="#i-trend"/></svg>
  <svg class="icon" style="left:342px;top:491px;width:22px;height:22px"><use href="#i-checkc"/></svg>
  <div class="card-title" style="left:16px;top:406px">Grant Application Support</div>
  <div class="card-title" style="left:341px;top:406px">Documentation Assistance</div>
  <div class="card-title" style="left:16px;top:522px">Project Planning</div>
  <div class="card-title" style="left:341px;top:522px">Implementation Support</div>
  <p class="small" style="left:16px;top:425px;width:285px">We assist facilities in identifying and applying for relevant turf management grants</p>
  <p class="small" style="left:341px;top:425px;width:290px">Complete documentation support for grant requirements and compliance</p>
  <p class="small" style="left:16px;top:541px;width:285px">Detailed project plans and cost estimates for grant applications</p>
  <p class="small" style="left:341px;top:541px;width:290px">Professional execution of approved grant-funded turf projects</p>

  <div style="left:0;top:599px;width:638px;height:308px;background:var(--soft)"></div>
  <h2 class="display c" style="left:0;top:622px;width:638px;font-size:17px">AVAILABLE GRANT PROGRAMS</h2>
  <div class="card" style="left:136px;top:653px;width:368px;height:69px"></div>
  <div class="card" style="left:136px;top:734px;width:368px;height:69px"></div>
  <div class="card" style="left:136px;top:816px;width:368px;height:69px"></div>
  <div style="left:148px;top:663px;font-size:11px;font-weight:500">State Government Sports Grants</div>
  <div style="left:148px;top:744px;font-size:11px;font-weight:500">Council Community Grants</div>
  <div style="left:148px;top:826px;font-size:11px;font-weight:500">National Sport Fund Grants</div>
  <p class="small" style="left:148px;top:687px;width:345px">State government funding for sports facility upgrades and maintenance projects, including turf improvement and field renovation.</p>
  <p class="small" style="left:148px;top:768px;width:345px">Local council funding opportunities for community sports facility improvements and ongoing maintenance programs.</p>
  <p class="small" style="left:148px;top:850px;width:345px">Federal funding programs supporting sports infrastructure development and facility improvements across Australia.</p>

  <div class="cta" style="left:0;top:939px;width:638px;height:136px"></div>
  <h2 class="display c on-green" style="left:0;top:962px;width:638px;font-size:16px">LET'S DISCUSS YOUR PROJECT</h2>
  <p class="lead c" style="left:170px;top:989px;width:298px">Contact us to explore grant opportunities and start planning your turf improvement project</p>
  <div class="btn-grey" style="left:266px;top:1033px;width:107px;height:18px;line-height:18px;font-size:7px">Schedule a Consultation</div>
</section>

<!-- AWARD PAGE -->
<section class="page page-award" style="left:1289px;top:200px;width:643px;height:1058px">
  <div class="nav" style="top:0;height:30px">
    <div class="brand" style="left:10px;top:8px">CFS</div>
    <div class="link" style="left:338px;top:8px">Home</div>
    <div class="link" style="left:372px;top:8px">Shop</div>
    <div class="link" style="left:405px;top:8px">Gallery</div>
    <div class="link" style="left:442px;top:8px">Grants Initiative</div>
    <div class="link on" style="left:508px;top:8px">Northreach Green</div>
    <div class="quote" style="left:589px;top:1px;width:54px;height:20px;line-height:20px">Get a Quote</div>
  </div>
  <svg class="icon" style="left:304px;top:42px;width:38px;height:38px;stroke-width:2"><use href="#i-trophy"/></svg>
  <h1 class="display c" style="left:0;top:88px;width:647px;font-size:27px;letter-spacing:2px">NORTHREACH FINEST GREEN</h1>
  <p class="sub c" style="left:0;top:131px;width:647px">Celebrating excellence in sports turf maintenance across the Mackay region</p>
  <div style="left:108px;top:176px;width:430px;height:126px;border:1.5px solid var(--green);border-radius:3px;background:var(--white)"></div>
  <div class="c" style="left:108px;top:188px;width:430px;font-size:14px;font-weight:500">About the Initiative</div>
  <p class="small" style="left:121px;top:216px;width:405px">Northreach Finest Green is an annual initiative recognizing outstanding sports turf maintenance and management across our region's sporting facilities.</p>
  <p class="small" style="left:121px;top:247px;width:405px">This program celebrates the dedication of facility managers, groundskeepers, and organizations who maintain exceptional playing surfaces that contribute to player safety, performance, and the overall sporting experience.</p>
  <p style="left:121px;top:278px;font-size:7.5px;font-weight:600">Join us in celebrating Northreach's finest sports fields and lawns!</p>

  <div class="card" style="left:4px;top:332px;width:204px;height:105px"></div>
  <div class="card" style="left:220px;top:332px;width:205px;height:105px"></div>
  <div class="card" style="left:437px;top:332px;width:206px;height:105px"></div>
  <svg class="icon" style="left:95px;top:348px;width:22px;height:22px"><use href="#i-star"/></svg>
  <svg class="icon" style="left:312px;top:348px;width:22px;height:22px"><use href="#i-award"/></svg>
  <svg class="icon" style="left:529px;top:348px;width:22px;height:22px"><use href="#i-users"/></svg>
  <div class="card-title c" style="left:4px;top:380px;width:204px">Recognition</div>
  <div class="card-title c" style="left:220px;top:380px;width:205px">Expert Assessment</div>
  <div class="card-title c" style="left:437px;top:380px;width:206px">Community Pride</div>
  <p class="small c" style="left:24px;top:398px;width:164px">Showcase your facility's commitment to excellence in turf management</p>
  <p class="small c" style="left:232px;top:398px;width:181px">Professional evaluation by industry experts and turf specialists</p>
  <p class="small c" style="left:452px;top:398px;width:176px">Celebrate our region's best sporting facilities together</p>

  <h2 class="display c" style="left:0;top:467px;width:647px;font-size:17px">PAST WINNERS</h2>
  <div class="card" style="left:139px;top:510px;width:368px;height:51px"></div>
  <div class="card" style="left:139px;top:568px;width:368px;height:51px"></div>
  <div class="card" style="left:139px;top:627px;width:368px;height:51px"></div>
  <div class="card-title" style="left:151px;top:522px">Pioneer Sports Complex</div>
  <div class="card-title" style="left:151px;top:580px">Regional Rugby Stadium</div>
  <div class="card-title" style="left:151px;top:639px">Community Softball Diamond</div>
  <div class="small" style="left:151px;top:537px">Soccer Field</div>
  <div class="small" style="left:151px;top:595px">Rugby League</div>
  <div class="small" style="left:151px;top:654px">Softball Field</div>
  <svg class="icon" style="left:479px;top:521px;width:15px;height:15px"><use href="#i-trophy"/></svg>
  <svg class="icon" style="left:479px;top:579px;width:15px;height:15px"><use href="#i-trophy"/></svg>
  <svg class="icon" style="left:479px;top:638px;width:15px;height:15px"><use href="#i-trophy"/></svg>
  <div style="left:478px;top:539px;font-size:6.5px;font-weight:600">2024</div>
  <div style="left:478px;top:597px;font-size:6.5px;font-weight:600">2024</div>
  <div style="left:478px;top:656px;font-size:6.5px;font-weight:600">2023</div>

  <div class="grass-soft" role="img" aria-label="Dew drops on green grass blades" style="left:4px;top:708px;width:639px;height:184px"></div>
  <h2 class="display" style="left:19px;top:748px;font-size:16px">CRITERIA FOR EXCELLENCE</h2>
  <div style="left:19px;top:776px;font-size:8.5px;line-height:21px;color:#333">
    <div style="position:static"><span style="position:static;color:var(--green)">✓</span>&nbsp; Consistent turf quality and appearance</div>
    <div style="position:static"><span style="position:static;color:var(--green)">✓</span>&nbsp; Effective maintenance practices and programs</div>
    <div style="position:static"><span style="position:static;color:var(--green)">✓</span>&nbsp; Player safety and performance considerations</div>
    <div style="position:static"><span style="position:static;color:var(--green)">✓</span>&nbsp; Environmental sustainability practices</div>
  </div>

  <div class="cta" style="left:4px;top:922px;width:639px;height:136px"></div>
  <h2 class="display c on-green" style="left:0;top:946px;width:647px;font-size:16px">NOMINATE YOUR FACILITY</h2>
  <p class="lead c" style="left:168px;top:972px;width:310px">Think your sports field deserves recognition? Submit your nomination for Northreach Finest Green</p>
  <div class="btn-grey" style="left:240px;top:1016px;width:90px;height:19px;line-height:19px;font-size:7px">Submit Nomination</div>
  <div class="btn-line" style="left:339px;top:1016px;width:67px;height:19px;line-height:17px;font-size:7px">Learn More</div>
</section>

<!-- GALLERY PAGE -->
<section class="page page-gallery" style="left:0;top:1270px;width:647px;height:572px">
  <div class="nav" style="top:0;height:37px">
    <div class="brand" style="left:14px;top:14px">CFS</div>
    <div class="link" style="left:342px;top:14px">Home</div>
    <div class="link" style="left:377px;top:14px">Shop</div>
    <div class="link on" style="left:409px;top:14px">Gallery</div>
    <div class="link" style="left:447px;top:14px">Grants Initiative</div>
    <div class="link" style="left:512px;top:14px">Northreach Green</div>
    <div class="quote" style="left:594px;top:9px;width:53px;height:19px">Get a Quote</div>
  </div>
  <h1 class="display c" style="left:0;top:47px;width:655px;font-size:29px;letter-spacing:2.5px">PROJECT GALLERY</h1>
  <p class="sub c" style="left:160px;top:85px;width:335px">Showcasing our professional turf management work across Mackay's premier sports facilities</p>
  <div class="btn-green" style="left:190px;top:135px;width:51px;height:18px;line-height:18px;font-size:7px">All Projects</div>
  <div class="card" style="left:246px;top:135px;width:41px;height:18px;line-height:16px;font-size:7px;text-align:center">Soccer</div>
  <div class="card" style="left:292px;top:135px;width:62px;height:18px;line-height:16px;font-size:7px;text-align:center">Rugby League</div>
  <div class="card" style="left:359px;top:135px;width:42px;height:18px;line-height:16px;font-size:7px;text-align:center">Softball</div>
  <div class="card" style="left:406px;top:135px;width:59px;height:18px;line-height:16px;font-size:7px;text-align:center">Maintenance</div>
  <div class="photo" role="img" aria-label="Photo: soccer field at sunset" style="left:8px;top:177px;width:205px;height:115px"></div>
  <div class="photo" role="img" aria-label="Photo: rugby league stadium field" style="left:224px;top:177px;width:206px;height:115px"></div>
  <div class="photo" role="img" aria-label="Photo: softball diamond from above" style="left:441px;top:177px;width:206px;height:115px"></div>
  <div class="photo" role="img" aria-label="Photo: grass blades with dew" style="left:8px;top:304px;width:205px;height:115px"></div>
  <div class="photo" role="img" aria-label="Photo: soccer pitch in evening light" style="left:224px;top:304px;width:206px;height:115px"></div>
  <div class="photo" role="img" aria-label="Photo: stadium field with line markings" style="left:441px;top:304px;width:206px;height:115px"></div>
  <div class="cta" style="left:8px;top:450px;width:639px;height:118px"></div>
  <h2 class="display c on-green" style="left:0;top:474px;width:655px;font-size:16px">READY TO TRANSFORM YOUR FIELD?</h2>
  <p class="lead c" style="left:0;top:500px;width:655px">Let us bring professional-grade turf management to your sports facility</p>
  <div class="btn-grey" style="left:284px;top:525px;width:87px;height:19px;line-height:19px;font-size:7px">Contact Us Today</div>
</section>

<!-- SHOP PAGE -->
<section class="page page-shop" style="left:655px;top:1280px;width:639px;height:415px">
  <div class="nav" style="top:-12px;height:30px">
    <div class="brand" style="left:6px;top:15px">CFS</div>
    <div class="link" style="left:335px;top:15px">Home</div>
    <div class="link on" style="left:369px;top:15px">Shop</div>
    <div class="link" style="left:401px;top:15px">Gallery</div>
    <div class="link" style="left:439px;top:15px">Grants Initiative</div>
    <div class="link" style="left:505px;top:15px">Northreach Green</div>
    <div class="quote" style="left:586px;top:10px;width:53px;height:19px">Get a Quote</div>
  </div>
  <h1 class="display c" style="left:0;top:37px;width:639px;font-size:28px;letter-spacing:2px">SHOP PRODUCTS &amp; SERVICES</h1>
  <p class="sub c" style="left:0;top:75px;width:639px">Professional turf management products and comprehensive service programs</p>
  <div style="left:0;top:112px;width:639px;height:18px;background:#efefef;border-radius:3px"></div>
  <div style="left:2px;top:114px;width:212px;height:14px;background:var(--white);border-radius:2px"></div>
  <div style="left:0;top:116px;width:215px;font-size:7px;text-align:center">Turf Products</div>
  <div style="left:215px;top:116px;width:210px;font-size:7px;text-align:center;color:#666">Turf Programs</div>
  <div style="left:425px;top:116px;width:212px;font-size:7px;text-align:center;color:#666">Supply &amp; Apply</div>

  <div class="card" style="left:0;top:146px;width:204px;height:123px"></div>
  <div class="card" style="left:217px;top:146px;width:205px;height:123px"></div>
  <div class="card" style="left:434px;top:146px;width:205px;height:123px"></div>
  <div style="left:12px;top:156px;font-size:11.5px;font-weight:500">Premium Fertilizer Blend</div>
  <div style="left:229px;top:156px;font-size:11.5px;font-weight:500">Turf Soil Conditioner</div>
  <div style="left:446px;top:156px;font-size:11.5px;font-weight:500">Pest Control Solution</div>
  <p class="small" style="left:12px;top:180px;width:185px">High-quality slow-release fertilizer for optimal turf growth</p>
  <p class="small" style="left:229px;top:180px;width:185px">Improves soil structure and water retention</p>
  <p class="small" style="left:446px;top:180px;width:185px">Eco-friendly pest management for sports turf</p>
  <div class="price" style="left:12px;top:210px">$199</div>
  <div class="price" style="left:229px;top:199px">$149</div>
  <div class="price" style="left:446px;top:199px">$179</div>
  <div class="btn-green" style="left:12px;top:238px;width:181px;height:19px;line-height:19px;font-size:7px"><svg class="cart-ico"><use href="#i-cart"/></svg>&nbsp;&nbsp;Add to Cart</div>
  <div class="btn-green" style="left:229px;top:227px;width:181px;height:19px;line-height:19px;font-size:7px"><svg class="cart-ico"><use href="#i-cart"/></svg>&nbsp;&nbsp;Add to Cart</div>
  <div class="btn-green" style="left:446px;top:227px;width:181px;height:19px;line-height:19px;font-size:7px"><svg class="cart-ico"><use href="#i-cart"/></svg>&nbsp;&nbsp;Add to Cart</div>

  <div style="left:0;top:300px;width:639px;height:111px;background:var(--soft);border-radius:3px"></div>
  <h2 class="display c" style="left:0;top:315px;width:639px;font-size:15px">NEED A CUSTOM SOLUTION?</h2>
  <p class="small c" style="left:158px;top:340px;width:323px">Every facility has unique requirements. Contact us for a personalized turf management plan.</p>
  <div class="btn-green" style="left:272px;top:375px;width:94px;height:20px;line-height:20px;font-size:7px">Get a Custom Quote</div>
</section>

</div>
</body>
</html>
```